Korvanta Brochure Design - IT Services - Modern Design - Services List

Hi,

We are looking for a modern IT Services brochure design of between 4 - 6 pages, it must be based on a blue and white colour theme with some nice technical imagery. It would need a section about why Korvanta and a contact section at the end.

Here is some info that could be included

Target Market(s)

Medium to Large Businesses

Industry/Entity Type

Information Technology

Colors
0054AA
0677BA
7BADD7
CADEEF
E8F1F8

Requirements
Must have
• Striking technical imagery
Nice to have
• Nice Icons to list the different services sections

```html
<!DOCTYPE html>
<html lang="en">
<head>
<meta charset="utf-8">
<title>Korvanta Brochure – Cover and Services Page</title>
<link rel="stylesheet" href="https://fonts.googleapis.com/css2?family=Ubuntu:wght@400;500;700&display=swap">
<style>
  :root {
    --canvas-bg: #a9a9a9;
    --cover-dark: #111821;
    --photo-top: #3c4f5a;
    --photo-mid: #24333d;
    --brand-blue: #1a8fd0;
    --band-blue: #1d93d2;
    --deep-blue: #0054aa;
    --pale-blue: #cadeef;
    --mist-blue: #e8f1f8;
    --tag-grey: #5d636b;
    --ink: #1b1b1f;
    --paper: #ffffff;
  }
  * { box-sizing: border-box; margin: 0; padding: 0; }
  html, body { width: 1200px; height: 1200px; overflow: hidden; }
  body {
    background: var(--canvas-bg);
    font-family: "Ubuntu", sans-serif;
    position: relative;
  }
  .page {
    position: absolute;
    top: 247px;
    width: 499px;
    height: 705px;
    overflow: hidden;
  }
  /* Cover */
  .cover { left: 82px; background: var(--cover-dark); }
  .cover-photo {
    position: absolute; left: 0; top: 0; width: 100%; height: 420px;
    background: linear-gradient(180deg, var(--photo-top) 0%, var(--photo-mid) 50%, var(--cover-dark) 100%);
  }
  .cover-brand {
    position: absolute; left: 80px; top: 510px;
    font-size: 52px; font-weight: 500; color: var(--brand-blue);
    letter-spacing: 1px; line-height: 1;
  }
  .cover-tagline {
    position: absolute; left: 227px; top: 572px;
    font-size: 15px; font-weight: 500; color: var(--tag-grey);
    letter-spacing: 0.3px;
  }
  /* Services page */
  .services-page { left: 620px; background: var(--paper); color: var(--ink); }
  .page-frame { position: absolute; inset: 0; }
  .wave-decor {
    position: absolute; left: 0; top: 20px; width: 430px; height: 120px;
    background: linear-gradient(90deg, rgba(29,147,210,0) 0%, rgba(29,147,210,0.35) 40%, rgba(29,147,210,0.25) 75%, rgba(29,147,210,0) 100%);
    border-radius: 50% 50% 40% 60% / 60% 40% 60% 40%;
  }
  .circuit-decor {
    position: absolute; left: 340px; top: 300px; width: 130px; height: 400px;
    background: linear-gradient(180deg, rgba(202,222,239,0) 0%, rgba(202,222,239,0.35) 50%, rgba(202,222,239,0) 100%);
  }
  .content { position: absolute; left: 29px; top: 150px; width: 445px; }
  .kicker { font-size: 13px; font-weight: 400; margin-bottom: 14px; }
  .title { font-size: 25px; font-weight: 700; color: var(--band-blue); margin-bottom: 14px; }
  .body-text { font-size: 10px; line-height: 12.6px; }
  .section-band {
    position: absolute; left: 0; top: 298px; width: 224px; height: 33px;
    background: var(--band-blue); color: var(--paper);
    font-size: 24px; font-weight: 500; padding: 3px 0 0 29px;
  }
  .service { position: absolute; left: 29px; width: 445px; }
  .service h3 { font-size: 14px; font-weight: 700; margin-bottom: 15px; }
  .service ul { list-style: none; margin-top: 14px; }
  .service li {
    position: relative; padding-left: 35px; font-size: 10px; line-height: 12.6px; margin-bottom: 5px;
  }
  .service li::before {
    content: "•"; position: absolute; left: 11px; top: 0;
  }
  .service-managed { top: 350px; }
  .service-cloud { top: 516px; }
</style>
</head>
<body>
  <section class="page cover">
    <div class="cover-photo" role="img" aria-label="Photograph of a dim IT operations centre with rows of monitor workstations behind glass walls"></div>
    <div class="cover-brand">Korvanta</div>
    <div class="cover-tagline">COMPUTING EXCELLENCE</div>
  </section>

  <section class="page services-page">
    <svg class="page-frame" width="499" height="705" viewBox="0 0 499 705" aria-hidden="true">
      <path d="M410 0 C455 20 478 70 478 180 L478 705 L499 705 L499 0 Z" fill="var(--band-blue)"/>
    </svg>
    <div class="wave-decor" role="img" aria-label="Flowing blue line wave decoration"></div>
    <div class="circuit-decor" role="img" aria-label="Faint circuit board line pattern"></div>

    <div class="content">
      <p class="kicker">Empowering Your Business with Cutting-Edge IT Solutions</p>
      <h1 class="title">About Korvanta</h1>
      <p class="body-text">At Korvanta, we are dedicated to providing top-tier IT services that drive efficiency, innovation, and growth for your business. With a commitment to excellence and a team of highly skilled professionals, we offer a comprehensive suite of solutions tailored to meet the unique needs of our clients.</p>
    </div>

    <h2 class="section-band">Our Services</h2>

    <div class="service service-managed">
      <h3>Managed IT Services</h3>
      <p class="body-text">Our Managed IT Services provide proactive monitoring and management of your IT infrastructure, ensuring maximum uptime and reliability. We offer:</p>
      <ul>
        <li>24/7 Network Monitoring: Continuous monitoring to detect and resolve issues before they impact your business.</li>
        <li>Helpdesk Support: Responsive and knowledgeable support team available round the clock.</li>
        <li>Patch Management: Regular updates and patches to keep your systems secure and up-to-date.</li>
        <li>IT Asset Management: Comprehensive tracking and management of your IT assets.</li>
      </ul>
    </div>

    <div class="service service-cloud">
      <h3>Cloud Solutions</h3>
      <p class="body-text">Embrace the power of the cloud with our scalable and secure cloud solutions. Our offerings include:</p>
      <ul>
        <li>Cloud Migration: Seamless transition of your applications and data to the cloud.</li>
        <li>Cloud Hosting: Reliable and scalable hosting solutions to meet your growing needs.</li>
        <li>Backup and Disaster Recovery: Robust backup and recovery solutions to ensure business continuity.</li>
        <li>Software as a Service (SaaS): Access to the latest software applications without the hassle of maintenance.</li>
      </ul>
    </div>
  </section>
</body>
</html>
```